Local Mortgage Broker requires DL Flyer

I Require DL sized design for local mortgage broker. Content that will go on the flyer is attached along with the logo.
Looking for a bright & catchy design with that little OOMPH.....on the creative side.
Am looking for a responsive campaign with this style of marketing. The main message is that "We may be able to save thousands of dollars for you, just give us a chance to review your mortgages"

Target Market(s)

All home owners with a mortgage or eople looking to buy their first home.

Industry/Entity Type

Marketing

```html
<!DOCTYPE html>
<html lang="en">
<head>
<meta charset="utf-8">
<title>NestWise Finance – DL Flyer</title>
<link rel="stylesheet" href="https://fonts.googleapis.com/css2?family=Open+Sans:wght@800&family=Asap:wght@400;600;700&display=swap">
<style>
  :root {
    --navy: #2a2a62;
    --yellow: #fff200;
    --white: #ffffff;
    --photo-light: #d9d4d0;
    --photo-mid: #b9aca6;
    --photo-warm: #d98a6a;
  }
  * { margin: 0; padding: 0; box-sizing: border-box; }
  html, body { width: 1200px; height: 2544px; overflow: hidden; background: var(--white); }
  .flyer {
    position: relative;
    width: 1200px;
    height: 2544px;
    background: var(--navy);
    font-family: "Asap", Arial, sans-serif;
    color: var(--white);
    overflow: hidden;
  }
  .headline {
    position: absolute;
    top: 0; left: 0; width: 100%; height: 329px;
    display: flex; flex-direction: column; justify-content: center; align-items: center;
    font-family: "Open Sans", Arial, sans-serif;
    font-weight: 800;
    font-size: 86px;
    line-height: 124px;
    letter-spacing: 1px;
    color: var(--yellow);
    text-align: center;
    padding-top: 6px;
  }
  .hero {
    position: absolute;
    top: 329px; left: 0; width: 1200px; height: 858px;
    background:
      radial-gradient(ellipse 320px 260px at 560px 460px, var(--photo-warm) 0%, rgba(217,138,106,0) 70%),
      linear-gradient(160deg, var(--photo-light) 0%, var(--photo-mid) 60%, #c9b8b0 100%);
  }
  .hero-caption {
    position: absolute;
    top: 1009px; left: 59px; width: 488px; height: 178px;
    background: var(--navy);
    display: flex; align-items: center; justify-content: center;
    text-align: center;
    font-weight: 700;
    font-size: 34px;
    line-height: 46px;
    padding: 0 30px;
  }
  .brand-corner {
    position: absolute;
    top: 806px; left: 583px; width: 617px; height: 381px;
  }
  .brand-name {
    position: absolute;
    top: 1085px; left: 680px; width: 470px;
    text-align: center;
    font-weight: 600;
    font-size: 56px;
    line-height: 70px;
    color: var(--navy);
  }
  .divider {
    position: absolute;
    top: 1187px; left: 0; width: 100%; height: 13px;
    background: var(--yellow);
  }
  .content {
    position: absolute;
    top: 1254px; left: 62px; width: 1090px;
  }
  .intro, .promise {
    font-size: 36.5px;
    line-height: 51px;
    font-weight: 400;
  }
  .services {
    list-style: none;
    margin-top: 44px;
    font-weight: 700;
    font-size: 36.5px;
    line-height: 51px;
    color: var(--yellow);
  }
  .services li::before { content: "•"; margin-right: 22px; }
  .promise { margin-top: 46px; }
  .call-to-action {
    position: absolute;
    top: 2060px; left: 0; width: 100%;
    text-align: center;
    font-weight: 700;
    font-size: 82px;
    line-height: 108px;
    color: var(--yellow);
  }
  .website {
    position: absolute;
    top: 2350px; left: 0; width: 100%;
    text-align: center;
    font-weight: 700;
    font-size: 51px;
    line-height: 70px;
    color: var(--yellow);
  }
  .footer-band {
    position: absolute;
    bottom: 0; left: 0; width: 100%; height: 64px;
    background: var(--yellow);
  }
</style>
</head>
<body>
<div class="flyer">
  <h1 class="headline"><span>FIND THE RIGHT</span><span>FINANCE SOLUTION</span></h1>

  <div class="hero" role="img" aria-label="Photo of a smiling woman holding a small model house with a red roof in her hands"></div>

  <p class="hero-caption">The right loan to suit your individual requirements.</p>

  <svg class="brand-corner" viewBox="0 0 617 381" aria-hidden="true">
    <polygon points="0,381 413,0 617,191 617,381" fill="#ffffff"/>
  </svg>
  <div class="brand-name">NestWise Finance</div>

  <div class="divider"></div>

  <section class="content">
    <p class="intro">Whether you are looking to buy your first home, renovate, refinance or invest, we’re here to negotiate the right finance for you.&nbsp; We’re a one-stop shop with hundreds of loan options available from across Australia’s leading lenders and we’ll work with you to find the right finance solution to meet your needs.</p>
    <ul class="services">
      <li>Refinance existing Mortgage</li>
      <li>Purchase First Home</li>
      <li>Purchase Investment Property</li>
      <li>Upgrade or Renovate existing Property</li>
    </ul>
    <p class="promise">We are confident that we may be able to save you thousands of dollars over the term of your loan by simply reviewing your existing home loan.</p>
  </section>

  <p class="call-to-action">Call us on 0412 555 018<br>To find out how!</p>

  <p class="website">www.nestwisefinance.com.au</p>

  <div class="footer-band"></div>
</div>
</body>
</html>
```